Buch-/eBook-Cover zum Thema Ökonomie
Ribo hat mit seinem Design genau meine Vorstellung getroffen! Einen Stern gibt's dafür Abzug, dass die verwendeten Programme und Fotos etc erst nach dem Zuschlag bekanntgegeben wurden - das hätte auch gleich transparent sein können. Aber grundsätzlich bin ich sehr zufrieden.
Zielgruppe
Ich bin mehrfacher Buchautor und Philosoph. Meine Zielgruppe hier sind jene, die sich für Ökonomie interessieren.
Aufgabenstellung
Ich will mein Buch 'Der Kreislauf der Nachfrage. Keiner bringt uns das Brot' auf Verlo BDS im Selfpublishing herausbringen. Dafür brauche ich eine druckfähige PDF-Datei. Ich habe Spezifikationen für die exakten Größen- und Seitenverhältnisse, die ich hochlade. Außerdem habe ich ein Logo (meine Q3T!), das an geeigneter Stelle auf dem Cover zu platzieren ist. Ich stelle mir grundsätzlich ein Bild von einer dominanten Spielfigur (wie beim Hüpf-und-schlag-den-Turm) vor, die auf einem Spielbrett steht, vielleicht mit anderen Spielfiguren im Hintergrund. Außerdem müssen Titel, Untertitel und mein Name (Konrad Edmund Wiesheimer) gut lesbar sein. Als Klappentext habe ich:
'Die Ökonomie beginnt nicht beim Markt – sie beginnt bei Ihnen.
Dieses Buch behauptet etwas Unverschämtes: Unsere Wirtschaft basiert auf der stillen Erwartung, dass jemand anderer uns füttert.
Wer das einmal sieht, versteht plötzlich Krisen, Macht und Wohlstand auf eine neue, fast unangenehme Weise.
Konrad Edmund Wiesheimer dreht die Perspektive radikal um – vom Verbraucher aus gedacht, bis nichts mehr selbstverständlich bleibt.
Ein Buch für alle, die nicht länger so tun wollen, als hätten sie mit dem Ganzen nichts zu tun.'
Ansonsten hoffe ich auf hochwertige, kreative Designergebnisse.
Das Design darf nicht zu überladen sein.

```html
<!DOCTYPE html>
<html lang="de">
<head>
<meta charset="utf-8">
<title>Der Kreislauf der Nachfrage – Umschlag</title>
<link href="https://fonts.googleapis.com/css2?family=Roboto:wght@300;400;500;700;900&display=swap" rel="stylesheet">
<style>
  :root {
    --ink-black: #050505;
    --board-blue: #6f8cb8;
    --board-light: #9fb5d6;
    --shadow-blue: #1c2a44;
    --piece-red: #8e1414;
    --text-white: #ffffff;
  }
  html, body {
    margin: 0;
    padding: 0;
    width: 1200px;
    height: 884px;
    overflow: hidden;
    background: var(--ink-black);
  }
  .cover-wrap {
    position: relative;
    width: 1200px;
    height: 884px;
    overflow: hidden;
    font-family: "Roboto", Arial, sans-serif;
    color: var(--text-white);
  }
  .scene-photo {
    position: absolute;
    inset: 0;
    background:
      radial-gradient(ellipse 220px 330px at 895px 520px, rgba(142,20,20,0.85), rgba(142,20,20,0) 100%),
      linear-gradient(172deg, var(--ink-black) 0%, var(--ink-black) 42%, var(--shadow-blue) 62%, var(--board-blue) 85%, var(--board-light) 100%);
  }
  .back-blurb {
    position: absolute;
    left: 87px;
    top: 80px;
    width: 440px;
    font-size: 19.5px;
    line-height: 25.3px;
    font-weight: 400;
    letter-spacing: 0.1px;
  }
  .back-blurb p { margin: 0 0 25px; }
  .barcode-area {
    position: absolute;
    left: 341px;
    top: 724px;
    width: 201px;
    height: 121px;
    background: var(--text-white);
  }
  .spine {
    position: absolute;
    left: 237px;
    top: 382px;
    width: 730px;
    height: 72px;
    transform: rotate(-90deg);
    transform-origin: center;
  }
  .spine-title {
    margin: 0;
    font-size: 34px;
    line-height: 36px;
    font-weight: 700;
    letter-spacing: 0.5px;
    text-transform: uppercase;
    white-space: nowrap;
  }
  .spine-subtitle {
    margin: 0;
    font-size: 24px;
    line-height: 28px;
    font-weight: 300;
    letter-spacing: 0.8px;
    text-transform: uppercase;
    white-space: nowrap;
  }
  .publisher-mark {
    position: absolute;
    font-family: "Roboto", Arial, sans-serif;
    font-weight: 700;
    color: var(--text-white);
    text-align: center;
    letter-spacing: 1px;
  }
  .publisher-mark--spine { left: 577px; top: 815px; width: 50px; font-size: 16px; }
  .publisher-mark--front { left: 876px; top: 810px; width: 70px; font-size: 22px; }
  .front-author {
    position: absolute;
    left: 660px;
    top: 46px;
    width: 502px;
    text-align: center;
    font-size: 41px;
    line-height: 40px;
    font-weight: 300;
    letter-spacing: 1px;
    text-transform: uppercase;
    margin: 0;
  }
  .front-title {
    position: absolute;
    left: 660px;
    top: 312px;
    width: 502px;
    margin: 0;
    text-align: center;
    font-size: 48px;
    line-height: 46px;
    font-weight: 900;
    letter-spacing: 0.5px;
    text-transform: uppercase;
  }
  .front-subtitle {
    position: absolute;
    left: 660px;
    top: 458px;
    width: 502px;
    margin: 0;
    text-align: center;
    font-size: 27px;
    line-height: 31px;
    font-weight: 500;
    letter-spacing: 0.6px;
    text-transform: uppercase;
  }
</style>
</head>
<body>
  <div class="cover-wrap">
    <div class="scene-photo" role="img" aria-label="Foto: eine große rote Spielfigur auf einem blau beleuchteten Spielbrett, unscharf im Hintergrund eine gelbe und eine blaue Figur, langer Schatten nach links"></div>

    <section class="back-blurb">
      <p>Die Ökonomie beginnt nicht beim Markt –<br>sie beginnt bei Ihnen.</p>
      <p>Dieses Buch behauptet etwas Unverschämtes: Unsere Wirtschaft basiert auf der stillen Erwartung, dass jemand anderer uns füttert.<br>
      Wer das einmal sieht, versteht plötzlich Krisen, Macht und Wohlstand auf eine neue, fast unangenehme Weise.<br>
      Konrad Edmund Wiesheimer dreht die Perspektive radikal um – vom Verbraucher aus gedacht, bis nichts mehr selbstverständlich bleibt.</p>
      <p>Ein Buch für alle, die nicht länger so tun wollen, als hätten sie mit dem Ganzen nichts zu tun</p>
    </section>

    <div class="barcode-area"></div>

    <div class="spine">
      <p class="spine-title">Der Kreislauf der Nachfrage</p>
      <p class="spine-subtitle">Keiner bringt uns das Brot</p>
    </div>
    <div class="publisher-mark publisher-mark--spine">Q3T</div>

    <p class="front-author">Konrad Edmund<br>Wiesheimer</p>
    <h1 class="front-title">Der<br>Kreislauf der<br>Nachfrage</h1>
    <p class="front-subtitle">Keiner bringt uns<br>das Brot</p>
    <div class="publisher-mark publisher-mark--front">Q3T</div>
  </div>
</body>
</html>
```